Business Card Re-Design for a Lighting Designer

I would like my business card re-designed. It is currently high gloss and they scratch too easily. I don not think the current design lends itself well to a matte finish. I have included the current design for reference along with our company logo.
Check out our website for current branding.
http://www.brenmoorastudio.example

Updates
Some of the top contenders are muslim and it is a holiday for them. I do not want to discriminate and would expect the same courtesy for holidays we celebrate.
Target Market(s)
Interior Designers, Architects
Contact Information for Business Card
Logo - Name, Title, Address, Telephone Number and Extension, Email
Font styles to use
Requirements
Must have
- All the information listed on the current business card. If you use Red, it needs to be the red from our logo.
Nice to have
- Vertical and Horizontal Designs will be entertained.
Should not have
- Requirements for a glossy finish...should not look too corporate since we are a design firm.

```html
<!DOCTYPE html>
<html lang="en">
<head>
<meta charset="utf-8">
<title>Brenmoora Studio — Business Card</title>
<link rel="stylesheet" href="https://fonts.googleapis.com/css2?family=Lato:wght@400;700&display=swap">
<style>
  :root {
    --brand-red: #9b1b1f;
    --ink-grey: #7a7a7a;
    --bar-grey: #9a9a9a;
    --card-white: #ffffff;
    --backdrop: #2b2b2b;
  }
  * { box-sizing: border-box; margin: 0; padding: 0; }
  html, body {
    width: 1200px; height: 900px; overflow: hidden;
    background: var(--backdrop);
    font-family: "Lato", sans-serif;
  }
  .canvas { position: relative; width: 1200px; height: 900px; }

  .card {
    position: absolute; left: 296px; width: 607px; height: 346px;
    overflow: hidden;
  }
  .card--front { top: 85px; background: var(--card-white); }
  .card--back  { top: 472px; background: var(--brand-red); }

  .wordmark {
    position: absolute; left: 30px; top: 28px;
    display: flex; align-items: center; gap: 10px;
    color: var(--brand-red); font-weight: 700; font-size: 22px;
    letter-spacing: 1px; line-height: 1.1;
  }
  .wordmark__square { width: 16px; height: 16px; background: var(--brand-red); }

  .person {
    position: absolute; right: 24px; top: 164px; text-align: right;
  }
  .person__name {
    color: var(--brand-red); font-weight: 700; font-size: 27px;
    letter-spacing: 0.3px; line-height: 1;
  }
  .person__title {
    margin-top: 6px; color: var(--ink-grey); font-size: 15px; letter-spacing: 0.5px;
  }

  .divider {
    position: absolute; left: 30px; right: 24px; top: 225px;
    height: 1px; background: var(--brand-red);
  }

  .contact {
    position: absolute; left: 30px; top: 248px;
    list-style: none; color: var(--ink-grey); font-size: 15px; line-height: 20px;
  }
  .contact li { display: flex; align-items: center; gap: 8px; }
  .contact svg { width: 11px; height: 11px; flex: none; }
  .contact .accent { color: var(--brand-red); }

  .address {
    position: absolute; right: 24px; top: 248px; text-align: right;
    font-style: normal; color: var(--ink-grey); font-size: 15px; line-height: 20px;
  }

  .edge-band { position: absolute; left: 0; bottom: 0; width: 607px; height: 22px; }

  .back-wordmark {
    position: absolute; left: 0; right: 0; top: 0; bottom: 0;
    display: flex; align-items: center; justify-content: center; gap: 14px;
    color: var(--card-white); font-weight: 700; font-size: 34px; letter-spacing: 2px;
  }
  .back-wordmark__square { width: 24px; height: 24px; background: var(--card-white); }
</style>
</head>
<body>
<main class="canvas">
  <section class="card card--front" aria-label="Card front">
    <div class="wordmark"><span class="wordmark__square"></span><span>BRENMOORA STUDIO</span></div>

    <div class="person">
      <h1 class="person__name">MAREN HOLLOWAY</h1>
      <p class="person__title">PRINCIPAL</p>
    </div>

    <div class="divider"></div>

    <ul class="contact">
      <li>
        <svg viewBox="0 0 12 12" aria-hidden="true"><path d="M3 1 L5 3.5 L4 5 Q5 7.5 7 8 L8.5 7 L11 9 L9.5 11 Q3 10.5 1 2.5 Z" fill="var(--brand-red)"/></svg>
        <span>555.014.2280 x1</span>
      </li>
      <li>
        <svg viewBox="0 0 12 12" aria-hidden="true"><rect x="1" y="2.5" width="10" height="7" fill="none" stroke="var(--brand-red)" stroke-width="1.3"/><path d="M1 2.5 L6 6.5 L11 2.5" fill="none" stroke="var(--brand-red)" stroke-width="1.3"/></svg>
        <span>maren@brenmoorastudio.example</span>
      </li>
      <li>
        <svg viewBox="0 0 12 12" aria-hidden="true"><circle cx="6" cy="6" r="5" fill="none" stroke="var(--brand-red)" stroke-width="1"/><ellipse cx="6" cy="6" rx="2.2" ry="5" fill="none" stroke="var(--brand-red)" stroke-width="0.8"/><path d="M1 6 H11 M2 3.5 H10 M2 8.5 H10" stroke="var(--brand-red)" stroke-width="0.8"/></svg>
        <span>www.<span class="accent">brenmoorastudio</span>.example</span>
      </li>
    </ul>

    <address class="address">
      218 Alder Row<br>
      Suite 40<br>
      Eugene, Oregon 97401
    </address>

    <svg class="edge-band" viewBox="0 0 607 22" aria-hidden="true">
      <rect x="0" y="15" width="330" height="7" fill="var(--bar-grey)"/>
      <polygon points="352,0 607,0 607,22 331,22" fill="var(--brand-red)"/>
    </svg>
  </section>

  <section class="card card--back" aria-label="Card back">
    <div class="back-wordmark"><span class="back-wordmark__square"></span><span>BRENMOORA STUDIO</span></div>
  </section>
</main>
</body>
</html>
```